FRESH WEB DESIGN FOR A HEALTH - SOCIAL NETWORK

We are currently looking for a creative, fresh, vibrant, inspiring design for a new social network focused on health and nutrition for health professionals (namely nutritionists) and end-users.

Design requirements - IMPORTANT: please see attached file 'LumaGrove web site design scope' for the detailed brief.

The web site requires new design templates with inter-changeable banners and in some cases profile images. It's important for the website to communicate LumaGrove's core values and image which includes fun, vitality, freshness, life fulfillment, trust, integrity and loyalty to the two target groups. Imagery must have a consistent/inter-related theme across all communities, topics and resources, which need to be easily applied to the web site.To help engage our audience we are looking for something fresh and unique in the selected imagery/ theme/ design templates.

The chosen design will need to be applied to create a PDF, PowerPoint and business card template.

Please see attached file 'LumaGrove web site design scope' to view the LumaGrove web site, which is currently under development.

Industry/Entity Type

Nutrition

```html
<!DOCTYPE html>
<html lang="en">
<head>
<meta charset="utf-8">
<title>LumaGrove – Making Health Simple</title>
<link href="https://fonts.googleapis.com/css2?family=Roboto:wght@300;400;500;700&display=swap" rel="stylesheet">
<style>
:root{
  --blue:#0b95d9;
  --blue-dark:#0a84c2;
  --blue-text:#1b8fd3;
  --green:#8cc63f;
  --green-text:#6aa21c;
  --ink:#2c2c2c;
  --muted:#6d6d6d;
  --rule:#e2e2e2;
  --page-bg:#f4f4f4;
  --hero-bg:#ebebeb;
  --white:#ffffff;
}
*{margin:0;padding:0;box-sizing:border-box}
html,body{width:817px;height:1200px;overflow:hidden}
body{background:var(--page-bg);font-family:'Roboto',Arial,sans-serif;color:var(--ink);position:relative}
.page{position:absolute;left:128px;top:0;width:560px;height:1200px;background:var(--white);box-shadow:0 0 6px rgba(0,0,0,.15)}
.abs{position:absolute}
.photo{border:3px solid var(--white);box-shadow:0 1px 4px rgba(0,0,0,.25)}

/* hero */
.hero{left:0;top:0;width:560px;height:310px;background:linear-gradient(#efefef,#e4e4e4)}
.brand{left:12px;top:14px;display:flex;align-items:center;gap:6px}
.brand-mark{width:28px;height:28px;border-radius:50%;background:var(--green)}
.brand-name{font-size:26px;font-weight:500;color:var(--green-text)}
.brand-tag{left:52px;top:51px;font-size:8px;letter-spacing:1.2px;color:var(--muted)}
.hero-title{left:20px;top:133px;font-size:25px;font-weight:400;color:var(--blue-text);letter-spacing:.5px}
.hero-sub{left:20px;top:162px;font-size:12px;letter-spacing:1.6px;color:#555}
.hero-dots{left:25px;top:253px;display:flex;gap:4px}
.hero-dots span{width:9px;height:9px;border-radius:50%;background:#b3b3b3}
.hero-dots span.active{background:#555;width:10px;height:10px;margin-top:-1px}
.hero-photo{left:154px;top:44px;width:406px;height:266px;background:linear-gradient(120deg,#d9d2c9,#b8b3ae 45%,#e3e2e6)}

/* nav */
.nav{left:0;top:310px;width:560px;height:30px;background:var(--blue);display:flex;align-items:center;padding-left:20px}
.nav a{color:var(--white);font-size:9.5px;text-decoration:none;margin-right:22px}
.search{left:422px;top:316px;width:82px;height:18px;background:var(--white)}
.search-btn{left:504px;top:316px;width:36px;height:18px;background:var(--green);color:var(--white);font-size:8px;text-align:center;line-height:18px}

/* features */
.feature{top:372px;width:160px}
.feature h3{font-size:12px;font-weight:400;display:flex;align-items:center;gap:7px;height:20px}
.feature p{margin-top:10px;font-size:8px;line-height:11.5px;color:var(--muted)}
.icon{width:19px;height:19px;flex:none}
.rule{height:1px;background:var(--rule)}

/* support */
.support-photo{left:14px;top:486px;width:146px;height:100px;background:linear-gradient(135deg,#f1e8df,#e2c9a8 50%,#f4f0eb)}
.support-body{left:177px;top:488px;width:170px}
.support-body h2{font-size:12px;font-weight:400;color:var(--blue-text)}
.support-body p{margin-top:10px;font-size:8px;line-height:11.5px;color:var(--muted)}
.more{font-size:8px;font-weight:700;color:var(--green-text);margin-top:7px;display:block}
.support-list{left:372px;top:478px;width:176px;height:132px;border-left:1px solid var(--rule);padding-left:9px;padding-top:14px}
.support-list h4{font-size:8px;font-weight:400;color:var(--green-text);margin-bottom:14px}
.support-list li{list-style:none;font-size:8px;color:var(--muted);margin-bottom:19px;display:flex;align-items:center;gap:4px}

/* sections */
.section-title{font-size:12px;font-weight:400;color:var(--ink)}
.card{width:102px}
.card .thumb{height:53px;width:102px}
.card h5{margin-top:12px;font-size:8px;font-weight:500;color:var(--ink)}
.card p{margin-top:3px;font-size:7.5px;line-height:10.5px;color:var(--muted)}
.view-all{font-size:8px;font-weight:700;color:var(--green-text)}
.res-title{left:384px;top:648px;display:flex;align-items:center;gap:5px}
.res{left:383px;width:170px;display:flex;gap:5px}
.res .thumb{width:36px;height:30px;flex:none}
.res h6{font-size:7.5px;font-weight:700;color:var(--ink)}
.res p{font-size:7.5px;line-height:10px;color:var(--muted);margin-top:1px}

/* footer */
.footer{left:0;top:1007px;width:560px;height:173px;background:var(--blue)}
.footer-col{top:1007px;height:173px;color:var(--white)}
.divider{top:1020px;width:3px;height:150px;background:linear-gradient(90deg,rgba(0,0,0,.12),transparent)}
.footer h3{font-size:12px;font-weight:400;color:var(--white)}
.post{display:flex;align-items:center;gap:9px;height:22px;border-bottom:1px solid rgba(255,255,255,.15);font-size:8px;color:#dff2fc}
.post .thumb{width:22px;height:18px;border:1px solid var(--white);flex:none}
.contact-row{display:flex;align-items:flex-start;gap:7px;font-size:8px;line-height:10px;color:var(--white)}
.social{display:flex;gap:14px}
.social span{width:9px;height:9px;border-radius:50%;background:var(--white)}
.newsletter-field{width:161px;height:20px;background:var(--white);font-size:7.5px;color:#aaa;padding-left:10px;line-height:20px}
.footer-brand{display:flex;align-items:center;gap:5px;opacity:.35}
.footer-brand .brand-mark{width:18px;height:18px;background:var(--white)}
.footer-brand span{font-size:17px;font-weight:500;color:var(--white)}
.submit{width:48px;height:18px;border:1px solid var(--white);border-radius:3px;font-size:8px;text-align:center;line-height:16px;color:var(--white)}
.copyright{left:0;top:1180px;width:560px;height:20px;background:var(--green);color:var(--white);font-size:7.5px;text-align:center;line-height:20px}
</style>
</head>
<body>
<div class="page">

  <header class="abs hero">
    <div class="abs brand"><span class="brand-mark"></span><span class="brand-name">LumaGrove</span></div>
    <div class="abs brand-tag">Making Health Simple...</div>
    <div class="abs hero-photo" role="img" aria-label="Three smiling colleagues gathered around a laptop"></div>
    <h1 class="abs hero-title">SHARE YOUR STORY</h1>
    <div class="abs hero-sub">AND SUPPORT OTHERS</div>
    <div class="abs hero-dots"><span></span><span></span><span></span><span></span><span class="active"></span></div>
  </header>

  <nav class="abs nav"><a>Home</a><a>Pages</a><a>Features</a><a>Blog</a><a>Portfolio</a><a>Community</a></nav>
  <div class="abs search"></div>
  <div class="abs search-btn">Search</div>

  <section class="abs feature" style="left:14px">
    <h3><svg class="icon" viewBox="0 0 20 20"><circle cx="10" cy="10" r="9" fill="#777"/><path d="M5 8c2-1 3 1 5 0s2 3 0 5-3 1-4-1z" fill="#fff"/></svg>Live-in Care</h3>
    <p>Mauris tristique ex at nisi tincidunt, sed accumsan sapien suscipit. Nulla rhoncus, nulla sit amet consequat tempor</p>
  </section>
  <section class="abs feature" style="left:200px">
    <h3><svg class="icon" viewBox="0 0 20 20"><circle cx="11" cy="10" r="8" fill="none" stroke="#777" stroke-width="1.5" stroke-dasharray="36 8"/><text x="6.5" y="13" font-size="7" font-weight="700" fill="#777" font-family="Roboto,sans-serif">24</text></svg>Daily Support</h3>
    <p>Mauris tristique ex at nisi tincidunt, sed accumsan sapien suscipit. Nulla rhoncus, nulla sit amet consequat tempor</p>
  </section>
  <section class="abs feature" style="left:386px">
    <h3><svg class="icon" viewBox="0 0 20 20" fill="#777"><circle cx="10" cy="6" r="3"/><circle cx="4" cy="8" r="2.3"/><circle cx="16" cy="8" r="2.3"/><path d="M5 17c0-4 2-6 5-6s5 2 5 6z"/><path d="M0 16c0-3 2-5 4-5s3 1 3 1l-2 4z"/><path d="M20 16c0-3-2-5-4-5s-3 1-3 1l2 4z"/></svg>Professional Assistance</h3>
    <p>Mauris tristique ex at nisi tincidunt, sed accumsan sapien suscipit. Nulla rhoncus, nulla sit amet consequat tempor</p>
  </section>

  <div class="abs rule" style="left:14px;top:459px;width:532px"></div>

  <div class="abs photo support-photo" role="img" aria-label="Woman in workout clothes relaxing with fresh fruit"></div>
  <article class="abs support-body">
    <h2>Support And Educate</h2>
    <p>Mauris tristique ex at nisi tincidunt, sed accumsan sapien suscipit. Nulla rhoncus, nulla sit amet consequat tempor, odio mi iaculis ipsum, eget porta risus enim sed ante. Aenean laoreet, neque id interdum</p>
    <span class="more">read more »</span>
  </article>
  <aside class="abs support-list">
    <h4>Support And Educate</h4>
    <ul>
      <li><svg width="8" height="6" viewBox="0 0 8 6" fill="none" stroke="#8cc63f"><path d="M1 1l2 2-2 2M4 1l2 2-2 2"/></svg>Health Problems Question Answer</li>
      <li><svg width="8" height="6" viewBox="0 0 8 6" fill="none" stroke="#8cc63f"><path d="M1 1l2 2-2 2M4 1l2 2-2 2"/></svg>Appropriate Health Care For Adults</li>
      <li><svg width="8" height="6" viewBox="0 0 8 6" fill="none" stroke="#8cc63f"><path d="M1 1l2 2-2 2M4 1l2 2-2 2"/></svg>Nursing Services</li>
    </ul>
  </aside>

  <div class="abs rule" style="left:14px;top:617px;width:532px"></div>

  <h2 class="abs section-title" style="left:16px;top:649px">Nutritional Therapists</h2>
  <div class="abs card" style="left:14px;top:673px"><div class="thumb photo" style="background:linear-gradient(135deg,#f3ede6,#e0b79a)" role="img" aria-label="Smiling woman holding an apple"></div><h5>Nam Dapibus Rhons Risus</h5><p>Aenean vel mollis lectus. Fus ce scelerisque ipsum ut nisi blandit volutpat...</p></div>
  <div class="abs card" style="left:132px;top:673px"><div class="thumb photo" style="background:linear-gradient(135deg,#eef0f1,#d6d0c8)" role="img" aria-label="Woman choosing between healthy foods"></div><h5>Nam Dapibus Rhons Risus</h5><p>Aenean vel mollis lectus. Fus ce scelerisque ipsum ut nisi blandit volutpat...</p></div>
  <div class="abs card" style="left:251px;top:673px"><div class="thumb photo" style="background:linear-gradient(135deg,#e9e3d2,#c9d87a 60%,#f0c060)" role="img" aria-label="Smiling woman with fresh fruit"></div><h5>Nam Dapibus Rhons Risus</h5><p>Aenean vel mollis lectus. Fus ce scelerisque ipsum ut nisi blandit volutpat...</p></div>
  <span class="abs view-all" style="left:14px;top:788px">View all »</span>

  <div class="abs rule" style="left:14px;top:820px;width:338px"></div>

  <h2 class="abs section-title" style="left:16px;top:836px">Success Stories</h2>
  <div class="abs card" style="left:14px;top:860px"><div class="thumb" style="background:linear-gradient(135deg,#e8e6e4,#8a6e5a 50%,#d9dde0)" role="img" aria-label="Woman in consultation with a professional"></div><h5>Nam Dapibus Rhons Risus</h5><p>Aenean vel mollis lectus. Fus ce scelerisque ipsum ut nisi blandit volutpat...</p></div>
  <div class="abs card" style="left:132px;top:860px"><div class="thumb" style="background:linear-gradient(135deg,#6f9a3e,#c9c2b6 50%,#5e8a3a)" role="img" aria-label="Senior woman smiling outdoors"></div><h5>Nam Dapibus Rhons Risus</h5><p>Aenean vel mollis lectus. Fus ce scelerisque ipsum ut nisi blandit volutpat...</p></div>
  <div class="abs card" style="left:251px;top:860px"><div class="thumb" style="background:linear-gradient(135deg,#3a3a24,#8a6f4e 50%,#2e2a1e)" role="img" aria-label="Portrait of a young woman"></div><h5>Nam Dapibus Rhons Risus</h5><p>Aenean vel mollis lectus. Fus ce scelerisque ipsum ut nisi blandit volutpat...</p></div>
  <span class="abs view-all" style="left:14px;top:975px">View all »</span>

  <h2 class="abs section-title res-title"><svg width="15" height="15" viewBox="0 0 15 15"><circle cx="7.5" cy="7.5" r="7" fill="#0b95d9"/><path d="M7.5 4v7M4 7.5h7" stroke="#fff" stroke-width="2"/></svg>Available Resources</h2>
  <div class="abs res" style="top:683px"><div class="thumb photo" style="background:linear-gradient(135deg,#efe3d3,#d9a25a)" role="img" aria-label="Family sharing a meal"></div><div><h6>Aliquam lacinia nunc eget cons</h6><p>Curabitur malesuada tempor mi ut finibus. Aliquam porttitor est erat, nec sagittis tellus dignissim ut.</p></div></div>
  <div class="abs res" style="top:740px"><div class="thumb photo" style="background:linear-gradient(135deg,#e6dccf,#b79a7e)" role="img" aria-label="Hands holding a small model house"></div><div><h6>Aliquam lacinia nunc eget cons</h6><p>Curabitur malesuada tempor mi ut finibus. Aliquam porttitor est erat, nec sagittis tellus dignissim ut.</p></div></div>
  <div class="abs res" style="top:796px"><div class="thumb photo" style="background:linear-gradient(135deg,#3f3a36,#a48b73)" role="img" aria-label="Person working at a desk"></div><div><h6>Aliquam lacinia nunc eget cons</h6><p>Curabitur malesuada tempor mi ut finibus. Aliquam porttitor est erat, nec sagittis tellus dignissim ut.</p></div></div>
  <div class="abs res" style="top:852px"><div class="thumb photo" style="background:linear-gradient(135deg,#f4e9d0,#e77b2a 50%,#8cc63f)" role="img" aria-label="Assorted fresh fruit and vegetables"></div><div><h6>Aliquam lacinia nunc eget cons</h6><p>Curabitur malesuada tempor mi ut finibus. Aliquam porttitor est erat, nec sagittis tellus dignissim ut.</p></div></div>
  <div class="abs res" style="top:912px"><div class="thumb photo" style="background:linear-gradient(135deg,#f1ecea,#e0a8b4)" role="img" aria-label="Woman holding a green vegetable"></div><div><h6>Aliquam lacinia nunc eget cons</h6><p>Curabitur malesuada tempor mi ut finibus. Aliquam porttitor est erat, nec sagittis tellus dignissim ut.</p></div></div>
  <span class="abs view-all" style="left:383px;top:975px">View all »</span>

  <footer class="abs footer"></footer>
  <div class="abs divider" style="left:190px"></div>
  <div class="abs divider" style="left:370px"></div>

  <div class="abs footer-col" style="left:14px;width:168px">
    <h3 style="margin-top:24px">Latest Post</h3>
    <div style="margin-top:11px">
      <div class="post"><span class="thumb" style="background:#e6c9a6" role="img" aria-label="Post thumbnail"></span>Curabitur ac neque at arcu vesti</div>
      <div class="post"><span class="thumb" style="background:#c99778" role="img" aria-label="Post thumbnail"></span>Proin vel mauris diam habitasse</div>
      <div class="post"><span class="thumb" style="background:#d88a6e" role="img" aria-label="Post thumbnail"></span>Proin urna enim semper posuere</div>
      <div class="post"><span class="thumb" style="background:#e9c28d" role="img" aria-label="Post thumbnail"></span>Nunc adipiscing semper nisl</div>
    </div>
    <span class="abs" style="left:133px;top:146px;font-size:8px;text-decoration:underline">View all »</span>
  </div>

  <div class="abs footer-col" style="left:205px;width:160px">
    <h3 style="margin-top:24px">Contact Us</h3>
    <div class="contact-row" style="margin-top:14px"><svg width="9" height="9" viewBox="0 0 10 10" fill="#fff"><path d="M5 0L0 5h1.5v5h2.5V7h2v3h2.5V5H10z"/></svg><span>345- Cras mattis facilisis lectus, ultricies ultrices velit pulvinar at</span></div>
    <div class="contact-row" style="margin-top:10px"><svg width="9" height="9" viewBox="0 0 10 10" fill="#fff"><path d="M2 0l2 2.5-1.2 1.5c.6 1.4 1.8 2.6 3.2 3.2L7.5 6 10 8l-1.5 2C4 10 0 6 0 1.5z"/></svg><span>(800)555-0142</span></div>
    <div class="contact-row" style="margin-top:11px"><svg width="9" height="7" viewBox="0 0 10 7"><rect width="10" height="7" fill="#fff"/><path d="M0 0l5 4 5-4" fill="none" stroke="#0b95d9"/></svg><span>info@lumagrove.com</span></div>
    <div class="social" style="margin-top:20px"><span></span><span></span><span></span><span></span></div>
  </div>

  <div class="abs footer-col" style="left:384px;width:166px">
    <h3 style="margin-top:24px">Subscribe Newsletter</h3>
    <p style="margin-top:8px;font-size:8px;line-height:10px">Your email address to receive all news from our awesome website</p>
    <div class="newsletter-field" style="margin-top:15px;margin-left:2px">enter email address</div>
    <div class="abs footer-brand" style="left:8px;top:113px"><span class="brand-mark"></span><span>LumaGrove</span></div>
    <div class="abs submit" style="left:116px;top:114px">Submit</div>
  </div>

  <div class="abs copyright">Copyright © 2014, All rights reserved.</div>
</div>
</body>
</html>
```